Banner and Overlay for my twicth channel*

I need an overlay and banner for my twitch channel. My channel mostly play card game and some shooting game. I would like to see designs that use Yellow and Black. You can put something like skull and card in the designs. My channel name is KORVINE_Q.

Font styles to use
Sans Serif

Colors
ffffff

```html
<!DOCTYPE html>
<html lang="en">
<head>
<meta charset="utf-8">
<title>KORVINE_Q — Channel Banner</title>
<link rel="stylesheet" href="https://fonts.googleapis.com/css2?family=Michroma&display=swap">
<style>
  :root {
    --bg-deep: #140b24;
    --bg-mid: #2a1a45;
    --circuit-faint: #3a2a63;
    --neon-violet: #7b3cff;
    --neon-violet-core: #b58cff;
    --neon-gold: #f2c413;
    --neon-gold-core: #fff3b0;
    --stone-face: #e6e4d8;
    --stone-side: #74726a;
    --stone-edge: #55534c;
    --emblem-rust: #a86a2a;
    --emblem-dark: #3a2212;
    --white: #ffffff;
  }
  html, body {
    margin: 0;
    padding: 0;
    width: 1200px;
    height: 754px;
    overflow: hidden;
    background: var(--bg-deep);
  }
  .banner {
    position: relative;
    width: 1200px;
    height: 754px;
    overflow: hidden;
    background:
      radial-gradient(ellipse 60% 45% at 50% 50%, #35224f 0%, transparent 70%),
      radial-gradient(ellipse 30% 40% at 8% 55%, #2b1d44 0%, transparent 70%),
      linear-gradient(180deg, #120a20 0%, var(--bg-mid) 50%, #150c26 100%);
  }
  .banner svg { position: absolute; inset: 0; }
  .channel-name text {
    font-family: "Michroma", sans-serif;
    font-weight: 400;
  }
  .name-face { fill: var(--stone-face); }
  .name-side { fill: var(--stone-side); }
  .name-edge { fill: var(--stone-edge); }
</style>
</head>
<body>
<main class="banner">
  <svg width="1200" height="754" viewBox="0 0 1200 754" xmlns="http://www.w3.org/2000/svg">
    <defs>
      <filter id="glow-violet" x="-20%" y="-50%" width="140%" height="200%">
        <feGaussianBlur stdDeviation="5" result="b"/>
        <feMerge><feMergeNode in="b"/><feMergeNode in="b"/><feMergeNode in="SourceGraphic"/></feMerge>
      </filter>
      <filter id="glow-gold" x="-20%" y="-50%" width="140%" height="200%">
        <feGaussianBlur stdDeviation="4" result="b"/>
        <feMerge><feMergeNode in="b"/><feMergeNode in="b"/><feMergeNode in="SourceGraphic"/></feMerge>
      </filter>
      <linearGradient id="triangle-edge" x1="0" y1="0" x2="1" y2="1">
        <stop offset="0" stop-color="#e0c21a"/>
        <stop offset="0.6" stop-color="#6b3cd8"/>
        <stop offset="1" stop-color="#e0c21a"/>
      </linearGradient>
      <radialGradient id="emblem-fill" cx="0.5" cy="0.5" r="0.5">
        <stop offset="0" stop-color="#d08a3a"/>
        <stop offset="0.6" stop-color="#a86a2a"/>
        <stop offset="1" stop-color="#3a2212"/>
      </radialGradient>
    </defs>

    <g class="circuit-traces" fill="none" stroke="var(--circuit-faint)" stroke-width="1.2">
      <polyline points="0,48 52,48 82,16 132,16 186,72 250,72 300,30 440,16 760,16 790,30 910,30 1010,72 1060,24 1200,24"/>
      <polyline points="0,142 160,142 205,97 920,97 980,142 1200,142"/>
      <polyline points="0,262 290,262 330,232 880,232 920,262 1200,262"/>
      <polyline points="0,510 370,510 400,395 800,395 830,510 1200,510"/>
      <polyline points="0,560 60,560 70,552 460,552 490,590 740,590 760,552 1140,552 1200,580"/>
      <polyline points="0,740 120,740 190,630 1010,630 1080,740 1200,740"/>
    </g>

    <g class="neon-violet-trace" fill="none" filter="url(#glow-violet)">
      <polyline points="0,189 195,189 268,124 930,124 1005,189 1200,189" stroke="var(--neon-violet)" stroke-width="6"/>
      <polyline points="0,189 195,189 268,124 930,124 1005,189 1200,189" stroke="var(--neon-violet-core)" stroke-width="1.5"/>
      <line x1="295" y1="80" x2="915" y2="80" stroke="var(--neon-violet)" stroke-width="3" opacity="0.7"/>
    </g>

    <g class="emblem-triangles" fill="rgba(255,255,255,0.05)" stroke="url(#triangle-edge)" stroke-width="1.5">
      <polygon points="510,222 412,329 566,331"/>
      <polygon points="704,222 637,331 791,330"/>
    </g>

    <g class="emblem" role="img" aria-label="Channel emblem: skull inside a cog with crossed rifles">
      <ellipse cx="605" cy="195" rx="118" ry="105" fill="url(#emblem-fill)" opacity="0.85"/>
    </g>

    <g class="channel-name">
      <g class="name-edge" aria-hidden="true">
        <text x="166" y="516" font-size="190" textLength="700" lengthAdjust="spacingAndGlyphs">KORVINE</text>
        <text x="878" y="521" font-size="96" textLength="150" lengthAdjust="spacingAndGlyphs">_Q</text>
      </g>
      <g class="name-side" aria-hidden="true">
        <text x="168" y="514" font-size="190" textLength="700" lengthAdjust="spacingAndGlyphs">KORVINE</text>
        <text x="880" y="519" font-size="96" textLength="150" lengthAdjust="spacingAndGlyphs">_Q</text>
        <text x="170" y="512" font-size="190" textLength="700" lengthAdjust="spacingAndGlyphs">KORVINE</text>
        <text x="882" y="517" font-size="96" textLength="150" lengthAdjust="spacingAndGlyphs">_Q</text>
      </g>
      <g class="name-face">
        <text x="172" y="510" font-size="190" textLength="700" lengthAdjust="spacingAndGlyphs">KORVINE</text>
        <text x="884" y="515" font-size="96" textLength="150" lengthAdjust="spacingAndGlyphs">_Q</text>
      </g>
    </g>

    <g class="neon-gold-trace" fill="none" filter="url(#glow-gold)">
      <polyline points="0,600 180,600 222,580 980,580 1040,626 1200,626" stroke="var(--neon-gold)" stroke-width="5"/>
      <polyline points="0,600 180,600 222,580 980,580 1040,626 1200,626" stroke="var(--neon-gold-core)" stroke-width="1.2"/>
      <polyline points="0,697 112,697 160,660 260,660" stroke="var(--neon-gold)" stroke-width="3" opacity="0.8"/>
      <polyline points="940,660 1040,660 1100,697 1200,697" stroke="var(--neon-gold)" stroke-width="3" opacity="0.8"/>
    </g>

    <g class="suit-medallions" fill="none" stroke="var(--neon-gold)" stroke-width="4" filter="url(#glow-gold)" stroke-linejoin="round">
      <path d="M158,642 Q170,672 200,672 L262,672"/>
      <path d="M937,672 L1000,672 Q1030,672 1043,645"/>
      <circle cx="334" cy="672" r="73"/>
      <path class="suit-diamond" d="M334,630 L368,672 L334,714 L300,672 Z"/>
      <circle cx="511" cy="672" r="73"/>
      <path class="suit-club" d="M511,632 a17,17 0 0 1 14,27 a17,17 0 1 1 -6,28 l8,22 h-32 l8,-22 a17,17 0 1 1 -6,-28 a17,17 0 0 1 14,-27 Z"/>
      <circle cx="688" cy="672" r="73"/>
      <path class="suit-heart" d="M688,720 L652,682 a20,20 0 0 1 36,-30 a20,20 0 0 1 36,30 Z"/>
      <circle cx="865" cy="672" r="73"/>
      <path class="suit-spade" d="M865,627 C880,650 900,662 900,683 a18,18 0 0 1 -30,12 l8,22 h-26 l8,-22 a18,18 0 0 1 -30,-12 C830,662 850,650 865,627 Z"/>
    </g>
    <g class="suit-cores" fill="none" stroke="var(--white)" stroke-width="1.2" opacity="0.9" aria-hidden="true">
      <circle cx="334" cy="672" r="73"/>
      <circle cx="511" cy="672" r="73"/>
      <circle cx="688" cy="672" r="73"/>
      <circle cx="865" cy="672" r="73"/>
    </g>
  </svg>
</main>
</body>
</html>
```